Verdant Pathworks Business Card

want the back of card to be blue- with the logo in the center
front of card- info plus logo (info being mailing address, email address, and website address )
4 different names with titles to have on cards
1) Dominic Ashvale - Owner
2) Bethany Korvuth- Customer Relationship Specialist
3) Luca Brennwick- Vice President of Sales
4) Neil Umbright- Chief Technology Officer

Target Market(s)

tech company in the government/probation office industry

Industry/Entity Type

Government Office

Contact Information for Business Card

1) Dominic Ashvale - Owner

Colors
0355a3
ffffff

Requirements
Must have
• back side should be blue, with the logo placed in the center
• front side needs to include both the logo, as well as company info (info should include website address, email address, and mailing address)

```html
<!DOCTYPE html>
<html lang="en">
<head>
<meta charset="utf-8">
<title>Verdant Pathworks Business Cards</title>
<link rel="stylesheet" href="https://fonts.googleapis.com/css2?family=Open+Sans:wght@400;600;700&display=swap">
<style>
  :root {
    --brand-blue: #0355a3;
    --grey-band: #a7a9ac;
    --paper: #ffffff;
    --ink: #3a3a3a;
    --ink-soft: #555a60;
    --stage: #2b2b2b;
  }
  * { box-sizing: border-box; margin: 0; padding: 0; }
  html, body { width: 1200px; height: 2684px; overflow: hidden; }
  body { background: var(--stage); font-family: "Open Sans", sans-serif; }

  .card-set { position: relative; width: 1200px; height: 671px; }

  .card { position: absolute; width: 500px; height: 283px; border-radius: 15px; overflow: hidden; }

  .card-back { left: 110px; top: 30px; background: var(--brand-blue);
    display: flex; align-items: center; justify-content: center; }
  .card-back .brand-name { color: var(--paper); font-size: 36px; font-weight: 600; letter-spacing: 1px; }

  .card-front { left: 590px; top: 345px; background: var(--paper); }
  .card-front .wave { position: absolute; inset: 0; width: 100%; height: 100%; }
  .card-front .brand-name { position: absolute; right: 32px; top: 34px;
    color: var(--brand-blue); font-size: 21px; font-weight: 600; line-height: 1.2; }
  .card-front .rule { position: absolute; left: 32px; right: 32px; top: 84px; height: 1.5px; background: var(--brand-blue); }

  .person { position: absolute; left: 32px; top: 104px; }
  .person-name { color: var(--brand-blue); font-size: 17px; font-weight: 700; line-height: 1.2; }
  .person-title { color: var(--ink); font-size: 12px; line-height: 1.3; }

  .contact-list { position: absolute; left: 32px; top: 150px; list-style: none; }
  .contact-list li { display: flex; align-items: center; gap: 8px; color: var(--ink); font-size: 11px; line-height: 17px; }
  .contact-list svg { width: 10px; height: 10px; flex: none; }

  .address { position: absolute; right: 32px; top: 98px; text-align: right;
    color: var(--ink-soft); font-size: 11px; line-height: 1.4; }
  .website { position: absolute; right: 32px; top: 196px; color: var(--paper); font-size: 12px; font-weight: 600; }
</style>
</head>
<body>

<section class="card-set">
  <div class="card card-back"><span class="brand-name">Verdant Pathworks</span></div>
  <div class="card card-front">
    <svg class="wave" viewBox="0 0 500 283" preserveAspectRatio="none" aria-hidden="true">
      <path d="M0 228 C150 250 290 180 500 136 L500 283 L0 283 Z" fill="var(--grey-band)"/>
      <path d="M0 240 C155 262 300 192 500 150 L500 283 L0 283 Z" fill="var(--brand-blue)"/>
    </svg>
    <span class="brand-name">Verdant Pathworks</span>
    <div class="rule"></div>
    <div class="person">
      <p class="person-name">Bethany Korvuth</p>
      <p class="person-title">Customer Relationship Specialist</p>
    </div>
    <ul class="contact-list">
      <li><svg viewBox="0 0 12 12"><path d="M2 1 L4.5 1 L5 4 L3.6 5 C4.3 6.6 5.4 7.7 7 8.4 L8 7 L11 7.5 L11 10 C6 10.5 1.5 6 2 1Z" fill="var(--brand-blue)"/></svg>404-555-0183</li>
      <li><svg viewBox="0 0 12 12"><rect x="3" y="0.5" width="6" height="11" rx="1" fill="none" stroke="var(--brand-blue)" stroke-width="1.3"/><circle cx="6" cy="9.5" r="0.8" fill="var(--brand-blue)"/></svg>404-555-0127(office)</li>
      <li><svg viewBox="0 0 12 12"><rect x="0.5" y="2" width="11" height="8" fill="var(--brand-blue)"/><path d="M0.5 2 L6 6.5 L11.5 2" fill="none" stroke="#fff" stroke-width="1"/></svg>hello@verdantpathworks.com</li>
    </ul>
    <p class="address">Harlow Crossing<br>Emberfield Stanton, 2240</p>
    <p class="website">www.verdantpathworks.com</p>
  </div>
</section>

<section class="card-set">
  <div class="card card-back"><span class="brand-name">Verdant Pathworks</span></div>
  <div class="card card-front">
    <svg class="wave" viewBox="0 0 500 283" preserveAspectRatio="none" aria-hidden="true">
      <path d="M0 228 C150 250 290 180 500 136 L500 283 L0 283 Z" fill="var(--grey-band)"/>
      <path d="M0 240 C155 262 300 192 500 150 L500 283 L0 283 Z" fill="var(--brand-blue)"/>
    </svg>
    <span class="brand-name">Verdant Pathworks</span>
    <div class="rule"></div>
    <div class="person">
      <p class="person-name">Dominic Ashvale</p>
      <p class="person-title">Owner</p>
    </div>
    <ul class="contact-list">
      <li><svg viewBox="0 0 12 12"><path d="M2 1 L4.5 1 L5 4 L3.6 5 C4.3 6.6 5.4 7.7 7 8.4 L8 7 L11 7.5 L11 10 C6 10.5 1.5 6 2 1Z" fill="var(--brand-blue)"/></svg>404-555-0183</li>
      <li><svg viewBox="0 0 12 12"><rect x="3" y="0.5" width="6" height="11" rx="1" fill="none" stroke="var(--brand-blue)" stroke-width="1.3"/><circle cx="6" cy="9.5" r="0.8" fill="var(--brand-blue)"/></svg>404-555-0127(office)</li>
      <li><svg viewBox="0 0 12 12"><rect x="0.5" y="2" width="11" height="8" fill="var(--brand-blue)"/><path d="M0.5 2 L6 6.5 L11.5 2" fill="none" stroke="#fff" stroke-width="1"/></svg>hello@verdantpathworks.com</li>
    </ul>
    <p class="address">Harlow Crossing<br>Emberfield Stanton, 2240</p>
    <p class="website">www.verdantpathworks.com</p>
  </div>
</section>

<section class="card-set">
  <div class="card card-back"><span class="brand-name">Verdant Pathworks</span></div>
  <div class="card card-front">
    <svg class="wave" viewBox="0 0 500 283" preserveAspectRatio="none" aria-hidden="true">
      <path d="M0 228 C150 250 290 180 500 136 L500 283 L0 283 Z" fill="var(--grey-band)"/>
      <path d="M0 240 C155 262 300 192 500 150 L500 283 L0 283 Z" fill="var(--brand-blue)"/>
    </svg>
    <span class="brand-name">Verdant Pathworks</span>
    <div class="rule"></div>
    <div class="person">
      <p class="person-name">Luca Brennwick</p>
      <p class="person-title">Vice President of Sales</p>
    </div>
    <ul class="contact-list">
      <li><svg viewBox="0 0 12 12"><path d="M2 1 L4.5 1 L5 4 L3.6 5 C4.3 6.6 5.4 7.7 7 8.4 L8 7 L11 7.5 L11 10 C6 10.5 1.5 6 2 1Z" fill="var(--brand-blue)"/></svg>404-555-0183</li>
      <li><svg viewBox="0 0 12 12"><rect x="3" y="0.5" width="6" height="11" rx="1" fill="none" stroke="var(--brand-blue)" stroke-width="1.3"/><circle cx="6" cy="9.5" r="0.8" fill="var(--brand-blue)"/></svg>404-555-0127(office)</li>
      <li><svg viewBox="0 0 12 12"><rect x="0.5" y="2" width="11" height="8" fill="var(--brand-blue)"/><path d="M0.5 2 L6 6.5 L11.5 2" fill="none" stroke="#fff" stroke-width="1"/></svg>hello@verdantpathworks.com</li>
    </ul>
    <p class="address">Harlow Crossing<br>Emberfield Stanton, 2240</p>
    <p class="website">www.verdantpathworks.com</p>
  </div>
</section>

<section class="card-set">
  <div class="card card-back"><span class="brand-name">Verdant Pathworks</span></div>
  <div class="card card-front">
    <svg class="wave" viewBox="0 0 500 283" preserveAspectRatio="none" aria-hidden="true">
      <path d="M0 228 C150 250 290 180 500 136 L500 283 L0 283 Z" fill="var(--grey-band)"/>
      <path d="M0 240 C155 262 300 192 500 150 L500 283 L0 283 Z" fill="var(--brand-blue)"/>
    </svg>
    <span class="brand-name">Verdant Pathworks</span>
    <div class="rule"></div>
    <div class="person">
      <p class="person-name">Neil Umbright</p>
      <p class="person-title">Chief Technology Officer</p>
    </div>
    <ul class="contact-list">
      <li><svg viewBox="0 0 12 12"><path d="M2 1 L4.5 1 L5 4 L3.6 5 C4.3 6.6 5.4 7.7 7 8.4 L8 7 L11 7.5 L11 10 C6 10.5 1.5 6 2 1Z" fill="var(--brand-blue)"/></svg>404-555-0183</li>
      <li><svg viewBox="0 0 12 12"><rect x="3" y="0.5" width="6" height="11" rx="1" fill="none" stroke="var(--brand-blue)" stroke-width="1.3"/><circle cx="6" cy="9.5" r="0.8" fill="var(--brand-blue)"/></svg>404-555-0127(office)</li>
      <li><svg viewBox="0 0 12 12"><rect x="0.5" y="2" width="11" height="8" fill="var(--brand-blue)"/><path d="M0.5 2 L6 6.5 L11.5 2" fill="none" stroke="#fff" stroke-width="1"/></svg>hello@verdantpathworks.com</li>
    </ul>
    <p class="address">Harlow Crossing<br>Emberfield Stanton, 2240</p>
    <p class="website">www.verdantpathworks.com</p>
  </div>
</section>

</body>
</html>
```